Uregent Care opening postcard with coupon

We need a postcard created to mail directly to homes. The flyer need to be appealing and include a small spot with a coupon for $20 gift card with first visit. The post card needs to be 2 sided and 4X6. We have a logo. To learn more about us visit maplegroveclinicplus.example or check us out on facebook. I will try to figure out how to upload logo.

Target Market(s)

All households that need urgent care.

Industry/Entity Type

Healthcare

Font styles to use
Serif

Colors
33a6d7
447fba
85acd3
85cae6
cfdfed
ecf7fb

Requirements
Must have
• our logo
• family centered
• some services offered
• coupon with free $20 gc at first visit if you bring in this flyer
Nice to have
• visually appealing

```html
<!DOCTYPE html>
<html lang="en">
<head>
<meta charset="utf-8">
<title>Maple Grove Clinic Plus – Opening Postcard</title>
<link href="https://fonts.googleapis.com/css2?family=Open+Sans:wght@400;600;700;800&family=Roboto+Condensed:wght@400;700&display=swap" rel="stylesheet">
<style>
  :root{
    --sky:#33a6d7;
    --mid-blue:#447fba;
    --soft-blue:#85acd3;
    --aqua:#85cae6;
    --mist:#cfdfed;
    --ice:#ecf7fb;
    --navy:#2f3f96;
    --deep-navy:#1d2a5c;
    --bar-end:#2d64a0;
    --green:#8cc63f;
    --green-dark:#6fa62a;
    --page:#eceef0;
    --white:#ffffff;
  }
  *{box-sizing:border-box;margin:0;padding:0}
  html,body{width:886px;height:1200px;overflow:hidden}
  body{background:var(--page);font-family:"Open Sans",Arial,sans-serif;position:relative}
  .postcard{position:absolute;left:93px;width:700px;height:540px;background:var(--white);overflow:hidden;box-shadow:0 4px 14px rgba(0,0,0,.18)}
  .postcard--front{top:40px}
  .postcard--back{top:620px}
  .photo{position:absolute;background:linear-gradient(135deg,#d9d4cc 0%,#c98f86 35%,#b8473f 60%,#e7e3dc 100%)}
  .postcard--back .photo{background:linear-gradient(160deg,#6f8f4a 0%,#a7b98a 35%,#d8c6b4 60%,#8aa0b8 100%)}
  .curve{position:absolute;left:0;top:0}
  .brand{position:absolute;display:flex;align-items:center;gap:10px;font-family:"Open Sans",Arial,sans-serif;font-weight:800;color:var(--navy);font-size:25px;line-height:1.05}
  .brand__mark{width:22px;height:22px;background:var(--mid-blue);flex:none}
  .opening{position:absolute;left:444px;top:104px;font-weight:700;font-size:16px;color:var(--navy);letter-spacing:.2px}
  .coupon{position:absolute;background:linear-gradient(135deg,#f4f4f4,#dcdcdc);border:1px solid #c9c9c9;box-shadow:0 2px 4px rgba(0,0,0,.2);overflow:hidden}
  .coupon__ribbon{position:absolute;right:34px;top:-20px;width:14px;height:160px;background:var(--mid-blue);transform:rotate(-35deg)}
  .coupon__text{position:absolute;font-family:"Roboto Condensed",Arial,sans-serif;font-weight:400;color:var(--navy);line-height:1.15}
  .services{position:absolute;left:432px;top:276px;width:250px}
  .services__title{font-weight:700;font-size:12.5px;color:var(--navy);line-height:1.45;text-transform:uppercase}
  .services__list{list-style:none;margin-top:10px}
  .services__list li{position:relative;padding-left:26px;font-size:14px;color:var(--navy);line-height:18.4px}
  .services__list li::before{content:"";position:absolute;left:5px;top:5px;width:8px;height:8px;border-radius:50%;background:var(--soft-blue);border:2px solid var(--mist)}
  .badge{position:absolute;z-index:3;width:110px;height:110px;border-radius:50%;background:radial-gradient(circle at 40% 35%,#a6d64f,var(--green) 60%,var(--green-dark));display:flex;align-items:center;justify-content:center;text-align:center;color:var(--white);font-weight:700;font-size:11.5px;line-height:1.25;text-transform:uppercase;box-shadow:0 2px 5px rgba(0,0,0,.25)}
  .contact-bar{position:absolute;left:0;width:700px;height:66px;background:linear-gradient(90deg,var(--sky),var(--mid-blue) 70%,var(--bar-end));display:flex;align-items:center;padding-left:22px;color:var(--white);font-weight:700;font-size:14.2px;letter-spacing:.1px;text-transform:uppercase;white-space:nowrap}
  .contact-bar .sep{margin:0 8px}
  .family-band{position:absolute;left:0;top:296px;width:404px;height:42px;background:var(--navy);color:var(--white);font-weight:600;font-size:17px;display:flex;align-items:center;padding-left:135px;text-transform:uppercase}
  .info-panel{position:absolute;left:0;top:338px;width:402px;height:126px;background:linear-gradient(90deg,var(--mid-blue),#3f74b4)}
  .hours{position:absolute;left:240px;top:349px;color:var(--white);font-weight:700;font-size:10.5px;line-height:13.6px}
  .hours__title{text-transform:uppercase;font-size:11px}
  .stamp{position:absolute;left:587px;top:31px;width:92px;height:59px;border:1.5px solid #c8c8c8}
  .address-line{position:absolute;left:444px;width:235px;height:1.5px;background:#c8c8c8}
</style>
</head>
<body>

<section class="postcard postcard--front">
  <div class="photo" style="left:0;top:0;width:420px;height:472px" role="img" aria-label="Photo of a nurse taking a smiling older man's blood pressure"></div>
  <svg class="curve" width="700" height="472" viewBox="0 0 700 472" aria-hidden="true">
    <path d="M380 0 Q425 230 410 472 L700 472 L700 0 Z" fill="var(--white)"/>
    <path d="M372 0 Q418 230 402 472 L414 472 Q432 230 392 0 Z" fill="var(--aqua)"/>
  </svg>
  <div class="brand" style="left:420px;top:38px;width:270px">
    <span class="brand__mark"></span><span>Maple Grove<br>Clinic Plus</span>
  </div>
  <div class="opening">OPENING - OCTOBER 9TH</div>
  <div class="coupon" style="left:425px;top:135px;width:250px;height:127px">
    <div class="coupon__ribbon"></div>
    <div class="coupon__text" style="left:16px;top:48px;font-size:24px">$20 GIFT CARD<br>WITH FIRST VISIT</div>
  </div>
  <div class="services">
    <p class="services__title">We are here for your<br>everyday healthcare needs</p>
    <ul class="services__list">
      <li>Urgent Care</li>
      <li>Medication Refills</li>
      <li>Lab Tests &amp; Vaccinations</li>
      <li>Well Exams</li>
      <li>Health Screenings</li>
      <li>Pediatrics</li>
      <li>Infections</li>
      <li>Preventive Services</li>
    </ul>
  </div>
  <div class="contact-bar" style="top:474px">maplegroveclinicplus.example<span class="sep">|</span>4120 Harbor Lane Fairview<span class="sep">|</span>(555) 014-2290</div>
  <div class="badge" style="left:24px;top:360px">No<br>appointments<br>needed!</div>
</section>

<section class="postcard postcard--back">
  <div class="photo" style="left:0;top:110px;width:410px;height:186px" role="img" aria-label="Photo of a smiling family of five outdoors"></div>
  <div class="family-band">Family Centered</div>
  <div class="info-panel"></div>
  <svg class="curve" width="700" height="472" viewBox="0 0 700 472" aria-hidden="true">
    <path d="M376 0 Q418 220 400 464 L700 464 L700 0 Z" fill="var(--white)"/>
    <path d="M368 0 Q410 220 392 464 L404 464 Q424 220 388 0 Z" fill="var(--aqua)"/>
  </svg>
  <div class="brand" style="left:31px;top:38px;width:330px;font-size:29px">
    <span class="brand__mark"></span><span>Maple Grove<br>Clinic Plus</span>
  </div>
  <div class="coupon" style="left:22px;top:357px;width:197px;height:103px">
    <div class="coupon__ribbon" style="right:22px"></div>
    <div class="coupon__text" style="left:12px;top:40px;font-size:19px">$20 GIFT CARD<br>WITH FIRST VISIT</div>
  </div>
  <div class="hours">
    <div class="hours__title">Operating Hours</div>
    <div>Monday 7a-7p</div>
    <div>Tuesday 7a-7p</div>
    <div>Wednesday 7a-7p</div>
    <div>Thursday 7a-7p</div>
    <div>Friday 7a-7p</div>
    <div>Saturday 7a-7p</div>
    <div>Sunday 10a-7p</div>
  </div>
  <div class="stamp"></div>
  <div class="address-line" style="top:212px"></div>
  <div class="address-line" style="top:250px"></div>
  <div class="address-line" style="top:287px"></div>
  <div class="address-line" style="top:322px"></div>
  <div class="badge" style="left:328px;top:261px">No<br>appointments<br>needed!</div>
  <div class="contact-bar" style="top:474px">maplegroveclinicplus.example<span class="sep">|</span>4120 Harbor Lane Fairview<span class="sep">|</span>(555) 014-2290</div>
</section>

</body>
</html>
```